Varnel Disaster Response Team Van Wrap

Designing a wrap for our Disaster Response Team vans. We do flood, fire and mold insurance claim work. Looking for possible black fully wrapped van with large logo on the sides and on back of van. We will have to have the QADTM number and the LRW numbers in smaller letters along the bottom of sides and on back of van.
Updates

Wanting to give some extra time to designers to make some changes

Need extra days to review

Target Market(s)

Commerical and Residential Owners

Industry/Entity Type

Insurance restoration

Requirements
Must have
• 1-888-4VARNEL / www.varnelinc.example / FIRE / FLOOD / MOLD / ROOFING / QADTM # 52906431 / OK LRW # 61548820, Commercial Endorsement
Nice to have
• Want a full color wrap on a 2024 Halcor Brisk Voyanter 3500 EXT van. Maybe have a black background. The logo is black so may need to do some outlining for that. Also open to using one of the colors in the logo for the background. We do fire, flood, mold remediation and roofing. We will want the phone number and website to be in various places on sides and back.

```html
<!DOCTYPE html>
<html lang="en">
<head>
<meta charset="utf-8">
<title>Varnel Disaster Response Team – Van Wrap Side Panel</title>
<link rel="stylesheet" href="https://fonts.googleapis.com/css2?family=Montserrat:wght@700;800&family=Oswald:wght@600&display=swap">
<style>
  :root {
    --backdrop: #d9d9d9;
    --wrap-black: #111214;
    --wrap-charcoal: #3a3b3e;
    --sky-blue: #3aa3dc;
    --sky-light: #8fcdec;
    --alert-red: #c8304a;
    --alert-red-deep: #b02640;
    --accent-dot: #d9364f;
    --ink-white: #ffffff;
  }
  * { margin: 0; padding: 0; box-sizing: border-box; }
  html, body { width: 1200px; height: 800px; overflow: hidden; }
  body {
    background: var(--backdrop);
    font-family: "Montserrat", Arial, sans-serif;
    display: flex;
    align-items: center;
    justify-content: center;
  }
  .wrap-panel {
    position: relative;
    width: 1080px;
    height: 420px;
    border-radius: 18px;
    overflow: hidden;
    box-shadow: 0 10px 30px rgba(0,0,0,.18);
  }
  .wrap-panel__bands { position: absolute; inset: 0; }
  .brand-name {
    position: absolute;
    left: 300px; top: 130px;
    transform: rotate(-6deg);
    display: flex; align-items: center; gap: 18px;
    font-family: "Montserrat", Arial, sans-serif;
    font-weight: 800;
    font-size: 92px;
    letter-spacing: 4px;
    color: var(--ink-white);
    text-transform: uppercase;
  }
  .brand-name__dot {
    width: 26px; height: 26px; border-radius: 50%;
    background: var(--accent-dot);
  }
  .services {
    position: absolute;
    right: 40px; top: 70px;
    transform: rotate(-6deg);
    font-family: "Oswald", Arial, sans-serif;
    font-weight: 600;
    font-size: 44px;
    line-height: 1.15;
    color: var(--ink-white);
    text-align: left;
  }
  .services__dot { color: var(--accent-dot); font-size: 30px; vertical-align: middle; margin: 0 6px; }
  .contact {
    position: absolute;
    right: 40px; top: 210px;
    transform: rotate(-6deg);
    text-align: right;
    color: var(--ink-white);
    font-weight: 700;
  }
  .contact__web { font-size: 36px; letter-spacing: .5px; }
  .contact__phone { font-size: 48px; font-weight: 800; letter-spacing: 1px; }
  .audience {
    position: absolute;
    left: 70px; top: 320px;
    transform: rotate(-5deg);
    color: var(--ink-white);
    font-weight: 700;
    font-size: 22px;
    letter-spacing: 1.5px;
    line-height: 1.25;
    text-transform: uppercase;
  }
  .credentials {
    position: absolute;
    left: 40px; top: 235px;
    display: flex; align-items: center; gap: 10px;
    color: var(--ink-white);
    font-weight: 700;
    font-size: 14px;
    line-height: 1.35;
  }
  .credentials__badge {
    width: 34px; height: 34px;
    background: var(--ink-white);
    border-radius: 3px;
  }
</style>
</head>
<body>
  <main class="wrap-panel" aria-label="Varnel van wrap, driver side">
    <svg class="wrap-panel__bands" width="1080" height="420" viewBox="0 0 1080 420" aria-hidden="true">
      <rect width="1080" height="420" fill="var(--wrap-black)"/>
      <polygon points="0,0 1080,0 1080,40 680,80 640,60 300,60 0,150" fill="var(--sky-blue)"/>
      <polygon points="300,60 640,60 680,80 300,110" fill="var(--wrap-charcoal)"/>
      <polygon points="0,300 340,250 560,330 760,200 1080,160 1080,420 0,420" fill="var(--alert-red)"/>
      <rect y="350" width="1080" height="40" fill="var(--alert-red-deep)" opacity=".55"/>
    </svg>

    <div class="brand-name"><span class="brand-name__dot"></span>Varnel</div>

    <div class="services">
      <div>Fire<span class="services__dot">●</span>Flood</div>
      <div>Mold<span class="services__dot">●</span>Roofing</div>
    </div>

    <div class="contact">
      <div class="contact__web">varnelinc.example</div>
      <div class="contact__phone">1-888-4VARNEL</div>
    </div>

    <div class="credentials">
      <span class="credentials__badge" aria-hidden="true"></span>
      <div>QADTM # 52906431<br>OK LRW # 61548820</div>
    </div>

    <div class="audience">Commerical<br>&amp; Residential</div>
  </main>
</body>
</html>
```